Velmora - 3D medical animations and high end visual content

Our company creates high end visual content and animations for medical global companies.
Our website - www.velmora-studio.example
We would like to have an amazing business card for our CEO that he can use in the following exhebitions he is going to attend.
It is very important that the design will be memorable and diffrent. It has to reflect our brand design (you can have it from our website)
We would like to transmit innovation, prestige, luxury, aesthetics.
The card has to be Double Sided

Target Market(s)

Marketing managers in medical global companys

Industry/Entity Type

It Company

Contact Information for Business Card

Requirements
Nice to have
• It is very important that the design will be memorable and diffrent. It has to reflect our brand design (you can have it from our website)

```html
<!DOCTYPE html>
<html lang="en">
<head>
<meta charset="utf-8">
<title>Velmora – Business Card</title>
<link rel="stylesheet" href="https://fonts.googleapis.com/css2?family=Montserrat:wght@500;600&family=Open+Sans:wght@400;600;700&display=swap">
<style>
  :root{
    --backdrop:#2a2a2c;
    --card:#ffffff;
    --ink:#1d1d1f;
    --ink-soft:#4a4a4d;
    --teal:#0a8ea8;
    --teal-light:#12a3bd;
    --teal-deep:#0b7f96;
    --charcoal:#3a3a3c;
  }
  *{box-sizing:border-box;margin:0;padding:0}
  html,body{width:1200px;height:1000px;overflow:hidden}
  body{background:var(--backdrop);position:relative;font-family:"Open Sans",sans-serif}
  .card{
    position:absolute;left:320px;width:560px;height:320px;
    background:var(--card);border-radius:28px;overflow:hidden;
    box-shadow:0 14px 30px rgba(0,0,0,.35);
  }
  .card--front{top:150px}
  .card--back{top:530px}

  .wordmark{
    font-family:"Montserrat",sans-serif;font-weight:600;color:var(--ink);
    letter-spacing:3px;text-transform:uppercase;line-height:1;
    display:flex;align-items:center;gap:12px;
  }
  .wordmark__dot{width:14px;height:14px;border-radius:50%;background:var(--teal)}

  .front__brand{position:absolute;left:0;right:0;top:110px;display:flex;flex-direction:column;align-items:center}
  .front__brand .wordmark{font-size:44px}
  .brand-rule{width:300px;height:1px;background:var(--ink);margin:16px 0 12px}
  .front__url{font-size:13px;letter-spacing:3px;color:var(--ink-soft)}
  .front__url b{font-weight:400;color:var(--teal)}

  .back__shape{position:absolute;inset:0}
  .back__brand{position:absolute;left:190px;top:56px;display:flex;flex-direction:column;align-items:flex-start}
  .back__brand .wordmark{font-size:34px}
  .back__brand .brand-rule{width:270px;margin:12px 0 0}

  .person{position:absolute;left:166px;top:200px}
  .person__name{font-weight:700;font-size:19px;color:var(--ink-soft);letter-spacing:.5px;white-space:nowrap}
  .person__name span{color:var(--teal)}
  .person__title{font-size:13px;color:var(--ink-soft);margin-top:2px;letter-spacing:.5px}

  .divider{position:absolute;left:340px;top:144px;width:1px;height:78px;background:var(--teal)}

  .contacts{position:absolute;left:352px;top:142px;list-style:none;font-size:11px;color:var(--ink-soft)}
  .contacts li{display:flex;align-items:center;gap:7px;height:20px;white-space:nowrap}
  .contacts svg{width:11px;height:11px;fill:var(--teal);flex:none}
  .contacts b{font-weight:400;color:var(--teal)}
</style>
</head>
<body>

<section class="card card--front" aria-label="Card front">
  <div class="front__brand">
    <div class="wordmark"><span class="wordmark__dot"></span>Velmora</div>
    <div class="brand-rule"></div>
    <p class="front__url">www.<b>velmora-studio</b>.example</p>
  </div>
</section>

<section class="card card--back" aria-label="Card back">
  <svg class="back__shape" viewBox="0 0 560 320" preserveAspectRatio="none" aria-hidden="true">
    <rect width="560" height="320" fill="var(--charcoal)"/>
    <path d="M55 160 C45 230 90 290 180 320 H50 C30 260 35 200 55 160 Z" fill="var(--teal-deep)"/>
    <path d="M90 110 C70 200 110 280 220 320 H140 C70 270 60 190 90 110 Z" fill="var(--teal-light)"/>
    <path d="M200 0 H560 V320 H250 C140 280 110 140 200 0 Z" fill="var(--card)"/>
  </svg>

  <div class="back__brand">
    <div class="wordmark"><span class="wordmark__dot"></span>Velmora</div>
    <div class="brand-rule"></div>
  </div>

  <div class="person">
    <p class="person__name">NOAM <span>CASTELL</span></p>
    <p class="person__title">FOUNDER &amp; CEO</p>
  </div>

  <div class="divider"></div>

  <ul class="contacts">
    <li><svg viewBox="0 0 16 16"><path d="M2 5c0-2 3-3 6-3s6 1 6 3v2h-3V5.5H5V7H2zM3 8h10l1 6H2z"/></svg><span>+1-555-0142-881</span></li>
    <li><svg viewBox="0 0 16 16"><path d="M4 1l3 3-2 2c1 2 3 4 5 5l2-2 3 3-2 3C7 15 1 9 1 3z"/></svg><span>+1-555-0187-305</span></li>
    <li><svg viewBox="0 0 16 16"><path d="M1 3h14v10H1zM2 4l6 5 6-5v1L8 10 2 5z"/></svg><span>noam@velmora-studio.example</span></li>
    <li><svg viewBox="0 0 16 16"><circle cx="8" cy="8" r="7"/></svg><span>www.<b>velmora-studio</b>.example</span></li>
  </ul>
</section>

</body>
</html>
```